TrueGrindz Complete Stationery - Logo already designed

I already have the logo designed see attached. I need have a full set of stationary and business card designed for printing. I have attached an example of what I mean.

Please feel free to be creative. Also you can use the X in the logo by its self if you think it will work.

My details:

Name: Corwin Lestak
Social media handles: @corwinlestak
W: corwinlestak.com
E: info@corwinlestak.com
​P: 08 7493 5286
PO Box 7382, Halden Bay 6027
ABN 83 402 719 265

Target Market(s)

Anyone looking to be inspired.

Industry/Entity Type

Business

Font styles to use
Sans Serif

Colors
fbee3e
000000

Requirements
Must have
• My details:
• Name: Corwin Lestak
• Social media handles: @corwinlestak
• W: corwinlestak.com
• E: info@corwinlestak.com
• ​P: 08 7493 5286
• PO Box 7382, Halden Bay 6027
• ABN 83 402 719 265
Nice to have
• Something a little different
Should not have
• must not look tacky.

```html
<!DOCTYPE html>
<html lang="en">
<head>
<meta charset="utf-8">
<title>TrueGrindz Stationery</title>
<link rel="stylesheet" href="https://fonts.googleapis.com/css2?family=Bebas+Neue&family=Montserrat:wght@400;600&display=swap">
<style>
  :root {
    --bg: #efefef;
    --paper: #f7f7f7;
    --ink: #2f2c2c;
    --yellow: #e9c21b;
    --olive: #463d2b;
    --grey: #8a8a8a;
  }
  * { margin: 0; padding: 0; box-sizing: border-box; }
  html, body { width: 1200px; height: 795px; overflow: hidden; background: var(--bg); }
  .canvas { position: relative; width: 1200px; height: 795px; font-family: "Montserrat", sans-serif; }
  .piece { position: absolute; }
  .wordmark { font-family: "Bebas Neue", sans-serif; letter-spacing: .5px; line-height: 1; white-space: nowrap; }

  /* Letterhead */
  .letterhead { left: 292px; top: 99px; width: 293px; height: 415px; background: var(--paper); }
  .letterhead .wordmark { position: absolute; left: 24px; top: 26px; font-size: 17px; color: var(--ink); }
  .letterhead .contact { position: absolute; right: 18px; top: 24px; display: flex; gap: 5px; font-size: 4.2px; color: var(--grey); line-height: 7px; white-space: nowrap; }
  .contact .legal { text-align: right; padding-right: 5px; border-right: .6px solid var(--grey); }
  .contact .line { display: flex; align-items: center; gap: 3px; }
  .dot { width: 3.4px; height: 3.4px; border-radius: 50%; background: var(--yellow); display: inline-block; flex: none; }

  /* Folder */
  .folder { left: 636px; top: 80px; width: 346px; height: 437px; background: var(--ink); overflow: hidden; }
  .folder .tone { position: absolute; left: 60px; top: 0; width: 286px; height: 370px; background: var(--olive); }
  .folder .wordmark { position: absolute; left: 34px; top: 385px; font-size: 32px; color: #f2f2f2; }

  /* Business cards */
  .card-front { left: 100px; top: 572px; width: 75px; height: 132px; background: var(--ink); }
  .card-front .wordmark { position: absolute; right: 6px; top: 8px; font-size: 10px; color: var(--yellow); }
  .card-front .rule { position: absolute; left: 4px; top: 78px; width: 37px; height: .8px; background: #f2f2f2; }
  .card-front .name { position: absolute; left: 4px; top: 81px; font-family: "Bebas Neue", sans-serif; font-size: 6px; color: var(--yellow); white-space: nowrap; }
  .card-front .details { position: absolute; left: 4px; top: 91px; font-size: 3.3px; line-height: 5px; color: #cfcfcf; white-space: nowrap; }
  .card-front .details .line { display: flex; align-items: center; gap: 2px; }
  .card-front .dot { width: 2.6px; height: 2.6px; }
  .card-front .gap { height: 3px; }

  .card-back { left: 189px; top: 628px; width: 133px; height: 76px; background: var(--ink); }
  .card-back .wordmark { position: absolute; left: 0; right: 0; top: 29px; text-align: center; font-size: 18px; color: #f2f2f2; }
  .card-back .social { position: absolute; right: 6px; bottom: 5px; display: flex; gap: 2px; }
  .card-back .social .dot { width: 3.4px; height: 3.4px; }

  /* Envelopes */
  .envelope-front { left: 353px; top: 562px; width: 329px; height: 156px; background: var(--paper); }
  .envelope-front .wordmark { position: absolute; left: 15px; top: 13px; font-size: 21px; color: var(--ink); }
  .envelope-front .address { position: absolute; left: 15px; top: 41px; font-size: 4.4px; color: var(--grey); white-space: nowrap; }

  .envelope-back { left: 714px; top: 562px; width: 328px; height: 157px; background: var(--paper); }
  .envelope-back svg { position: absolute; left: 0; top: 0; }
  .envelope-back .wordmark { position: absolute; left: 0; right: 0; top: 14px; text-align: center; font-size: 15px; color: var(--yellow); }
</style>
</head>
<body>
<main class="canvas">

  <section class="piece letterhead" aria-label="Letterhead">
    <div class="wordmark">TrueGrindz</div>
    <div class="contact">
      <div class="legal">ABN 83 402 719 265<br>PO BOX 7382<br>HALDEN BAY 6027</div>
      <div>
        <div class="line"><span class="dot"></span>08 7493 5286</div>
        <div class="line"><span class="dot"></span>INFO@CORWINLESTAK.COM</div>
        <div class="line"><span class="dot"></span>WWW.CORWINLESTAK.COM</div>
      </div>
    </div>
  </section>

  <section class="piece folder" aria-label="Presentation folder">
    <div class="tone"></div>
    <div class="wordmark">TrueGrindz</div>
  </section>

  <section class="piece card-front" aria-label="Business card, details side">
    <div class="wordmark">TrueGrindz</div>
    <div class="rule"></div>
    <div class="name">CORWIN LESTAK</div>
    <div class="details">
      ABN 83 402 719 265<br>PO BOX 7382<br>HALDEN BAY 6027
      <div class="gap"></div>
      <div class="line"><span class="dot"></span>08 7493 5286</div>
      <div class="line"><span class="dot"></span>INFO@CORWINLESTAK.COM</div>
      <div class="line"><span class="dot"></span>WWW.CORWINLESTAK.COM</div>
    </div>
  </section>

  <section class="piece card-back" aria-label="Business card, brand side">
    <div class="wordmark">TrueGrindz</div>
    <div class="social"><span class="dot"></span><span class="dot"></span><span class="dot"></span></div>
  </section>

  <section class="piece envelope-front" aria-label="Envelope front">
    <div class="wordmark">TrueGrindz</div>
    <div class="address">PO BOX 7382, HALDEN BAY 6027</div>
  </section>

  <section class="piece envelope-back" aria-label="Envelope back">
    <svg width="328" height="157" viewBox="0 0 328 157">
      <path d="M0 0 H328 L322 58 Q321 68 311 68 H17 Q7 68 6 58 Z" fill="var(--ink)"/>
    </svg>
    <div class="wordmark">TrueGrindz</div>
  </section>

</main>
</body>
</html>
```